Business Card Design Project

New Private residential substance abuse treatment facility in Mapleton, UT. Facility located in elegant 11,000 home with stunning views of the mountains. Wish to incorporate colored logo. Business name- Birchwell Harbor Wellness. Facility is Tudor style with traditional furnishings, an overhead picture is attached. Lettering in a simple scroll or old english style. Must be easy to read with clear moderetly large font.
Updates

It seems the project time frame listed was not correct- it is a week.

Target Market(s)

Adults 18 and over with substance abuse issues requiring residential rehabilitation. Referral base are medical/mental health professionals, families and community agencies.

Industry/Entity Type

Residential

Colors
9bcb3b
fece3e
fbee3f

Requirements
Must have
• Clear and easy to read, professional and upscale presentation. Need logo, name, title, address, phone, fax and web page address. May add slogan later. Use same font as logo.
Nice to have
• Logo has a green mountain and a gold maple leaf so a nature themed element may work. Want to promote peaceful grounded image. Logo attached.
Should not have
• No tiny or complicated font. No modern or tech looking images. No light colored fonts.

```html
<!DOCTYPE html>
<html lang="en">
<head>
<meta charset="utf-8">
<title>Birchwell Harbor Wellness — Business Card</title>
<link rel="stylesheet" href="https://fonts.googleapis.com/css2?family=Tinos:wght@400;700&display=swap">
<style>
  :root {
    --stage: #f3f4f6;
    --card-light: #ffffff;
    --card-mid: #eef0f3;
    --card-shade: #d9dde3;
    --ink: #2b2b2b;
    --brand-ink: #3a3330;
    --title-green: #4f7a2a;
    --brand-dot: #6f9a3a;
    --icon-gold: #d9a13a;
    --sweep: rgba(255,255,255,0.85);
  }
  * { margin: 0; padding: 0; box-sizing: border-box; }
  html, body {
    width: 1200px; height: 900px; overflow: hidden;
    background: var(--stage);
  }
  .stage {
    position: relative; width: 1200px; height: 900px;
    display: flex; align-items: center; justify-content: center;
  }
  .business-card {
    position: relative; width: 1000px; height: 572px;
    border-radius: 30px; overflow: hidden;
    background: linear-gradient(160deg, var(--card-light) 0%, var(--card-light) 35%, var(--card-mid) 65%, var(--card-shade) 100%);
    box-shadow: 0 12px 40px rgba(0,0,0,0.12);
    font-family: "Tinos", "Times New Roman", serif;
    color: var(--ink);
  }
  .card-sweeps { position: absolute; inset: 0; width: 100%; height: 100%; }
  .brand {
    position: absolute; left: 70px; top: 128px;
    display: flex; align-items: center; gap: 18px;
  }
  .brand-mark {
    width: 54px; height: 54px; border-radius: 50%;
    background: var(--brand-dot); flex: none;
  }
  .brand-name {
    font-weight: 400; font-size: 46px; line-height: 1;
    color: var(--brand-ink); letter-spacing: 0.3px; white-space: nowrap;
  }
  .holder { position: absolute; right: 70px; top: 62px; text-align: right; }
  .holder-name { font-weight: 700; font-size: 24px; color: var(--ink); }
  .holder-title { font-weight: 700; font-size: 17px; color: var(--title-green); margin-top: 6px; }
  .contact-list {
    position: absolute; left: 70px; top: 318px; list-style: none;
    font-weight: 700; font-size: 26px; line-height: 1.2;
  }
  .contact-item { display: flex; align-items: flex-start; margin-bottom: 10px; }
  .contact-icon { width: 25px; height: 25px; margin-right: 14px; margin-top: 3px; flex: none; fill: var(--icon-gold); }
  .address-lines { display: block; }
</style>
</head>
<body>
<main class="stage">
  <article class="business-card">
    <svg class="card-sweeps" viewBox="0 0 1000 572" preserveAspectRatio="none" aria-hidden="true">
      <path d="M380 572 C 520 380, 720 250, 1000 190" fill="none" stroke="var(--sweep)" stroke-width="3"/>
      <path d="M300 572 C 480 360, 700 220, 1000 150" fill="none" stroke="var(--sweep)" stroke-width="1.5"/>
      <path d="M460 572 C 600 420, 780 300, 1000 250" fill="none" stroke="var(--sweep)" stroke-width="2"/>
    </svg>

    <div class="brand">
      <span class="brand-mark" aria-hidden="true"></span>
      <h1 class="brand-name">Birchwell Harbor Wellness</h1>
    </div>

    <div class="holder">
      <p class="holder-name">Dana Whitlock</p>
      <p class="holder-title">Manager</p>
    </div>

    <ul class="contact-list">
      <li class="contact-item">
        <svg class="contact-icon" viewBox="0 0 24 24" aria-label="Phone"><path d="M6.6 10.8a15 15 0 0 0 6.6 6.6l2.2-2.2c.3-.3.7-.4 1-.2 1.1.4 2.3.6 3.6.6.6 0 1 .4 1 1V20c0 .6-.4 1-1 1A17 17 0 0 1 3 4c0-.6.4-1 1-1h3.5c.6 0 1 .4 1 1 0 1.3.2 2.5.6 3.6.1.3 0 .7-.2 1z"/></svg>
        <span>555-210-4836</span>
      </li>
      <li class="contact-item">
        <svg class="contact-icon" viewBox="0 0 24 24" aria-label="Fax"><path d="M6 2h9l3 3v5H6z M3 11h18v9H3z"/><rect x="6" y="14" width="8" height="2" fill="#fff"/><circle cx="17.5" cy="15" r="1.3" fill="#fff"/></svg>
        <span>555-210-4857</span>
      </li>
      <li class="contact-item">
        <svg class="contact-icon" viewBox="0 0 24 24" aria-label="Email"><rect x="2" y="5" width="20" height="14" rx="2"/><path d="M3 6l9 7 9-7" fill="none" stroke="#fff" stroke-width="1.8"/></svg>
        <span>birchwell@mailpost.com</span>
      </li>
      <li class="contact-item">
        <svg class="contact-icon" viewBox="0 0 24 24" aria-label="Website"><circle cx="12" cy="12" r="10"/><g fill="none" stroke="#fff" stroke-width="1.4"><ellipse cx="12" cy="12" rx="4" ry="10"/><path d="M2 12h20M4 7h16M4 17h16"/></g></svg>
        <span>www.birchwellharbor.com</span>
      </li>
      <li class="contact-item">
        <svg class="contact-icon" viewBox="0 0 24 24" aria-label="Address"><path d="M12 3l10 9h-3v9h-5v-6h-4v6H5v-9H2z"/></svg>
        <span class="address-lines">4870 N. Alder Ridge Road,<br>Fernbrook, UT 84990</span>
      </li>
    </ul>
  </article>
</main>
</body>
</html>
```